VELNA BROCADE

Project name: “Velna Brocade” website
Objective: To create an elegant website,
intuitive and responsive to present this
what is “Velna Brocade”
See attached specifications.

```html
<!DOCTYPE html>
<html lang="en">
<head>
<meta charset="utf-8">
<title>Velna Brocade</title>
<link href="https://fonts.googleapis.com/css2?family=Playfair+Display:wght@500;600;700&family=Lato:wght@400;700&display=swap" rel="stylesheet">
<style>
:root{
  --green:#2f4f33;
  --green-soft:#4a6b4e;
  --mint:#eef8ee;
  --text:#333;
  --muted:#555;
  --white:#fff;
  --star:#e8b400;
}
*{box-sizing:border-box;margin:0;padding:0}
html,body{width:1200px;height:3674px;overflow:hidden;background:var(--white)}
body{font-family:'Lato',sans-serif;color:var(--text);position:relative}
.abs{position:absolute}
.serif{font-family:'Playfair Display',serif;color:var(--green)}
.btn{position:absolute;display:flex;align-items:center;justify-content:center;border-radius:30px;font-family:'Lato',sans-serif;font-weight:700;font-size:17px;background:var(--green);color:var(--white)}
/* top bar */
.topbar{left:332px;top:0;width:868px;height:41px;background:var(--green);border-bottom-left-radius:22px;color:var(--white);font-size:15px;display:flex;align-items:center}
.topbar span{position:absolute;display:flex;align-items:center;gap:8px}
.dot{width:20px;height:20px;border-radius:50%;background:var(--white)}
.stars{color:var(--star);letter-spacing:1px;font-size:14px}
.brand{left:111px;top:11px;width:150px;text-align:center}
.brand-mark{width:70px;height:70px;border:3px solid var(--green);border-radius:50%;margin:0 auto 8px}
.brand-name{font-weight:700;font-size:16px;letter-spacing:2.5px;color:var(--green)}
.nav a{position:absolute;top:70px;font-size:16px;color:var(--text);text-decoration:none}
.nav a.active{text-decoration:underline;color:var(--green)}
/* hero */
.hero{left:0;top:120px;width:1200px;height:600px;background:linear-gradient(180deg,#a9c3e0 0%,#dfe8f1 28%,#5f8a45 45%,#3f6a34 52%,#8fa6bd 60%,#6e8297 80%)}
.hero-castle{left:820px;top:150px;width:380px;height:420px;background:linear-gradient(180deg,#a08a6c,#6f6a4a 60%,#3f6a34);border-radius:40% 40% 10% 10%}
.hero h1{left:111px;top:195px;font-size:53px;line-height:64px;font-weight:600;width:620px}
.hero-sub{left:111px;top:346px;font-size:18px;color:#222}
/* about */
.about-photo{left:140px;top:782px;width:374px;height:374px;border-radius:50%;border:4px solid var(--green);background:linear-gradient(160deg,#b8cde0,#9c8b73 45%,#6f7d5a 80%)}
.about h2{left:644px;top:772px;font-size:41px;font-weight:600}
.about p{position:absolute;left:644px;width:445px;font-size:15px;line-height:25.7px;color:var(--muted);text-align:justify}
/* activities */
.act-title{left:0;width:1200px;top:1307px;text-align:center;font-size:40px;font-weight:600}
.act-photo{width:308px;height:308px;border-radius:50%;border:4px solid var(--green);top:1400px}
.act-label{top:1720px;width:340px;text-align:center;font-family:'Playfair Display',serif;font-size:22px;font-weight:600;color:#222}
.arrow{width:24px;height:24px;border:1.5px solid #444;border-radius:50%;top:1562px;display:flex;align-items:center;justify-content:center;font-size:13px;color:#444}
/* social */
.sec-title{left:0;width:1200px;text-align:center;font-size:40px;font-weight:600}
.feed{top:2003px;height:276px;border-radius:14px;box-shadow:0 2px 8px rgba(0,0,0,.2)}
/* cta */
.cta-title{left:0;width:1200px;top:2460px;text-align:center;font-size:40px;font-weight:600;color:var(--white)}
.cta-sub{left:0;width:1200px;top:2543px;text-align:center;font-size:18px;font-weight:700;color:var(--white)}
/* testimonials */
.card{top:2901px;width:310px;height:253px;border:1.5px solid #e4e4e4;border-radius:12px;box-shadow:0 2px 6px rgba(0,0,0,.1);padding:20px 22px}
.card .stars{font-size:18px;margin-left:30px}
.card .rate{display:flex;align-items:center;gap:0}
.card .rate .dot{border:2px solid #999;width:18px;height:18px}
.card p{margin-top:12px;font-size:14.5px;line-height:26.5px;color:var(--muted)}
.person{position:absolute;left:22px;top:170px;display:flex;align-items:center;gap:20px}
.avatar{width:70px;height:70px;border-radius:50%;background:linear-gradient(180deg,#d9d9d9,#9a9a9a)}
.person b{display:block;font-size:19px;color:#222;font-weight:700}
.person small{font-size:15px;color:var(--muted)}
/* footer */
.footer{left:0;top:3240px;width:1200px;height:434px;background:var(--green);color:var(--white)}
.foot-mark{left:541px;top:3332px;width:114px;height:114px;border-radius:50%;border:3px solid var(--white)}
.foot-name{left:0;width:1200px;top:3458px;text-align:center;font-size:26px;font-weight:700;letter-spacing:4px;color:var(--white)}
.foot-nav{left:0;width:1200px;top:3522px;display:flex;justify-content:center;gap:33px;font-size:15.5px;color:var(--white)}
.socials{left:0;width:1200px;top:3572px;display:flex;justify-content:center;gap:14px}
.socials i{width:21px;height:21px;border-radius:50%;background:var(--white);display:block}
.foot-rule{left:111px;top:3625px;width:978px;height:1px;background:rgba(255,255,255,.6)}
.legal{left:111px;top:3641px;font-size:15px;color:var(--white)}
.copy{right:111px;top:3641px;font-size:15px;color:var(--white)}
</style>
</head>
<body>

<!-- header -->
<div class="abs topbar">
  <span style="left:48px"><i class="dot"></i> 4.9 <b class="stars">★★★★★</b></span>
  <span style="left:242px">
    <svg width="18" height="18" viewBox="0 0 24 24"><path d="M6.6 10.8a15 15 0 0 0 6.6 6.6l2.2-2.2c.3-.3.7-.4 1-.2 1.1.4 2.3.6 3.6.6.6 0 1 .4 1 1V20c0 .6-.4 1-1 1A17 17 0 0 1 3 4c0-.6.4-1 1-1h3.5c.6 0 1 .4 1 1 0 1.3.2 2.5.6 3.6.1.3 0 .7-.2 1z" fill="#fff"/></svg>
    +1 555 014 2200</span>
  <span style="left:435px">
    <svg width="18" height="14" viewBox="0 0 18 14"><rect x="1" y="1" width="16" height="12" fill="none" stroke="#fff" stroke-width="1.6"/><path d="M1 1l8 7 8-7" fill="none" stroke="#fff" stroke-width="1.6"/></svg>
    info@velnabrocade.com</span>
  <span style="left:678px"><i style="width:32px;height:20px;background:linear-gradient(180deg,#c8102e 0 33%,#fff 33% 66%,#1f3f8f 66%);display:block"></i> EN ▾</span>
</div>

<div class="abs brand">
  <div class="brand-mark"></div>
  <div class="brand-name">VELNA BROCADE</div>
</div>

<nav class="nav">
  <a class="active" style="left:490px">Home</a>
  <a style="left:564px">About Us</a>
  <a style="left:659px">How We Help</a>
  <a style="left:786px">Land Prospecting</a>
</nav>
<div class="btn" style="left:943px;top:57px;width:146px;height:47px;font-size:18px">Contact Us</div>

<!-- hero -->
<section class="abs hero" role="img" aria-label="Lake in Limousin with a stone castle on a wooded shore under a cloudy sky"></section>
<div class="abs hero-castle" role="img" aria-label="Medieval stone castle with pointed towers"></div>
<svg class="abs" style="left:0;top:600px" width="1200" height="130" viewBox="0 0 1200 130">
  <path d="M0 25 Q600 150 1200 40 L1200 130 L0 130Z" fill="#fff"/>
  <path d="M0 25 Q600 150 1200 40 L1200 50 Q600 160 0 35Z" fill="var(--green)"/>
</svg>
<div class="hero">
  <h1 class="abs serif">Discover the Authentic Beauty of Limousin</h1>
  <div class="abs hero-sub">Connecting people, land, and possibilities.</div>
</div>
<div class="btn" style="left:111px;top:397px;width:172px;height:45px;border:1.5px solid #fff">Discover More</div>

<!-- about -->
<section class="about">
  <div class="abs about-photo" role="img" aria-label="Old stone village houses beside a curving riverside road"></div>
  <h2 class="abs serif">About Velna Brocade</h2>
  <p style="top:846px">Velna Brocade is dedicated to promoting the authentic beauty and opportunities of the Limousin region. We support families, couples, and future landowners in discovering the landscapes, lifestyle, and potential of this unique territory.</p>
  <p style="top:954px">connect people with land, guide them through their project, and showcase what makes Limousin an exceptional place to live. With strong local knowledge and trusted partnerships, Velna Brocade accompanies you at every step—from learning about the region to finding the land that fits your needs.</p>
  <div class="btn" style="left:644px;top:1106px;width:144px;height:44px">Read More</div>
</section>

<!-- activities -->
<svg class="abs" style="left:0;top:1225px" width="1200" height="625" viewBox="0 0 1200 625">
  <path d="M0 40 Q500 -20 1200 45 L1200 570 Q700 630 200 590 Q90 580 0 570Z" fill="var(--mint)"/>
  <path d="M0 30 Q500 -20 1200 35 L1200 45 Q500 -10 0 45Z" fill="var(--green)"/>
  <path d="M200 590 Q700 630 1200 570 L1200 590 Q700 650 200 600Z" fill="var(--green)"/>
</svg>
<h2 class="abs serif act-title">Activities to Do in Limousin</h2>
<div class="abs arrow" style="left:39px">‹</div>
<div class="abs arrow" style="left:1137px">›</div>
<div class="abs act-photo" style="left:113px;background:linear-gradient(180deg,#d9dccf,#6a7448 55%,#4d4a3e)" role="img" aria-label="Group of hikers reading a map on a forest trail"></div>
<div class="abs act-photo" style="left:445px;background:linear-gradient(180deg,#3f86d6,#b4cfe8 35%,#9a4a3a 50%,#4f7a34 75%)" role="img" aria-label="Red stone historic village among green hills"></div>
<div class="abs act-photo" style="left:779px;background:linear-gradient(180deg,#cfc9bd,#8f8a78 50%,#5a6b3a)" role="img" aria-label="Herd of zebras grazing in a natural park"></div>
<div class="abs act-label" style="left:97px">Hiking &amp; Nature Trails</div>
<div class="abs act-label" style="left:429px">Discover Historic Villages</div>
<div class="abs act-label" style="left:763px">Wildlife &amp; Natural Parks</div>

<!-- social feed -->
<h2 class="abs serif sec-title" style="top:1910px">Stay Connected With Velna Brocade</h2>
<div class="abs feed" style="left:111px;width:232px;background:linear-gradient(180deg,#8fb3e0,#8a7c66 40%,#55713a)" role="img" aria-label="Ivy covered stone manor tower"></div>
<div class="abs feed" style="left:358px;width:234px;background:linear-gradient(180deg,#4f6a55,#3d5a3e)" role="img" aria-label="Castle tower among trees behind a green overlay"><i class="dot abs" style="right:22px;top:20px;width:30px;height:30px"></i></div>
<div class="abs feed" style="left:608px;width:232px;background:linear-gradient(135deg,#8a8a7a,#5f7a3c 50%,#9a8a70)" role="img" aria-label="Aerial view of a village road winding through gardens"></div>
<div class="abs feed" style="left:856px;width:233px;background:linear-gradient(180deg,#b9d2ef,#a1543e 45%,#6a8a45 80%)" role="img" aria-label="Red sandstone village street with greenery"></div>

<!-- call to action -->
<svg class="abs" style="left:0;top:2388px" width="1200" height="345" viewBox="0 0 1200 345" role="img" aria-label="Aerial landscape of Limousin fields and villages under a green tint">
  <defs><linearGradient id="ctaFill" x1="0" y1="0" x2="0" y2="1"><stop offset="0" stop-color="#476a4d"/><stop offset="1" stop-color="#2f4f33"/></linearGradient></defs>
  <path d="M0 30 Q600 -25 1200 30 L1200 320 Q600 380 0 320Z" fill="url(#ctaFill)"/>
</svg>
<h2 class="abs serif cta-title">Ready to Start Your Project in Limousin?</h2>
<div class="abs cta-sub">We're here to answer your questions and guide you every step of the way.</div>
<div class="btn" style="left:527px;top:2600px;width:145px;height:46px;background:#fff;color:var(--green);font-weight:400">Contact Us</div>

<!-- testimonials -->
<h2 class="abs serif sec-title" style="top:2803px">Testimonials for Velna Brocade</h2>
<div class="abs card" style="left:111px">
  <div class="rate"><i class="dot"></i><span class="stars">★★★★★</span></div>
  <p>“Velna Brocade helped us discover a part of France we didn't know existed. Thanks to their guidance, we found the perfect land to build our family home.</p>
  <div class="person"><i class="avatar" role="img" aria-label="Portrait photo of reviewer"></i><div><b>Marc D.</b><small>Lille</small></div></div>
</div>
<div class="abs card" style="left:445px">
  <div class="rate"><i class="dot"></i><span class="stars">★★★★★</span></div>
  <p>“Beyond helping us find land, Velna Brocade showed us the beauty and lifestyle of the region. Their passion for Limousin is contagious!”</p>
  <div class="person"><i class="avatar" role="img" aria-label="Portrait photo of reviewer"></i><div><b>Julien P.</b><small>Nantes</small></div></div>
</div>
<div class="abs card" style="left:779px">
  <div class="rate"><i class="dot"></i><span class="stars">★★★★★</span></div>
  <p>“A very professional team. They guided us step-by-step and connected us with the right partners. We highly recommend their services.”</p>
  <div class="person"><i class="avatar" role="img" aria-label="Portrait photo of reviewer"></i><div><b>Claire M.</b><small>Toulouse</small></div></div>
</div>

<!-- footer -->
<svg class="abs" style="left:0;top:3230px" width="1200" height="50" viewBox="0 0 1200 50">
  <path d="M0 35 Q600 -20 1200 35 L1200 50 L0 50Z" fill="var(--green)"/>
</svg>
<footer class="abs footer" style="top:3262px;height:412px"></footer>
<div class="abs foot-mark"></div>
<div class="abs foot-name">VELNA BROCADE</div>
<div class="abs foot-nav"><span>Home</span><span>About Us</span><span>How We Help</span><span>Land Prospecting</span><span>Contact Us</span></div>
<div class="abs socials"><i></i><i></i><i></i><i></i></div>
<div class="abs foot-rule"></div>
<div class="abs legal">Privacy Policy &nbsp;| &nbsp;Terms &amp; Conditions &nbsp;| &nbsp;Cookie Policy</div>
<div class="abs copy">© 2025 Velna Brocade. All Rights Reserved</div>

</body>
</html>
```